Residential Construction Business - Site Signage

I need a design made for a site fence banner. We have a logo and branding so the design would need to be aligned with this. It would need to be made to specific size ratio so that it can be sent to the maker for production.
ratio : 4600 wide x 1700 high
The design should feature our website and also the slogan
"don't move, re-imagine"

Target Market(s)

potential clients

Industry/Entity Type

construction

Font styles to use
Other font styles liked:
• to match branding

Colors
0054AA
0677BA
7BADD7
CADEEF
E8F1F8

Requirements
Must have
• www.velmbuild.com.au Majority of the sign is our brand logo
Nice to have
• Majority of the sign is our brand logo
Should not have
• colors and themes that arent brand relevant

```html
<!DOCTYPE html>
<html lang="en">
<head>
<meta charset="utf-8">
<title>Velm Build – Site Fence Banner</title>
<link href="https://fonts.googleapis.com/css2?family=Montserrat:wght@500;600;700&display=swap" rel="stylesheet">
<style>
  :root {
    --navy: #0b3a5e;
    --page: #ececec;
    --white: #ffffff;
    --slate: #b7bfd4;
    --photo-warm: #b89a74;
    --photo-cool: #d9dbd6;
    --photo-dark: #2a2f38;
  }
  html, body {
    margin: 0;
    padding: 0;
    width: 1058px;
    height: 1200px;
    overflow: hidden;
    background: var(--page);
  }
  .canvas {
    position: relative;
    width: 1058px;
    height: 1200px;
  }
  .banner {
    position: absolute;
    left: 29px;
    top: 415px;
    width: 1000px;
    height: 370px;
    background: var(--white);
    overflow: hidden;
    font-family: "Montserrat", sans-serif;
    color: var(--navy);
  }
  .brand {
    position: absolute;
    left: 44px;
    top: 24px;
    display: flex;
    align-items: center;
    gap: 18px;
  }
  .brand-square {
    width: 112px;
    height: 112px;
    background: var(--navy);
  }
  .brand-name {
    font-weight: 700;
    font-size: 30px;
    letter-spacing: 7px;
    color: var(--navy);
    white-space: nowrap;
  }
  .slogan {
    position: absolute;
    left: 42px;
    top: 160px;
    margin: 0;
    font-weight: 700;
    font-size: 50px;
    line-height: 50px;
    letter-spacing: 0.5px;
    text-transform: uppercase;
  }
  .rule {
    position: absolute;
    left: 46px;
    top: 286px;
    width: 63px;
    height: 3px;
    background: var(--navy);
  }
  .contact {
    position: absolute;
    left: 46px;
    top: 300px;
    font-weight: 700;
    font-size: 20px;
    line-height: 24px;
  }
  .contact span { display: block; }
  .accent-strip {
    position: absolute;
    inset: 0;
    background: linear-gradient(90deg, rgba(255,255,255,0) 0%, var(--slate) 100%);
    clip-path: polygon(495px 0, 540px 0, 452px 370px, 420px 370px);
  }
  .photo {
    position: absolute;
    inset: 0;
    clip-path: polygon(535px 0, 1000px 0, 1000px 370px, 448px 370px);
    background: linear-gradient(90deg, var(--photo-cool) 0%, var(--photo-warm) 40%, var(--photo-cool) 62%, var(--photo-dark) 78%, var(--photo-warm) 100%);
  }
</style>
</head>
<body>
<div class="canvas">
  <div class="banner">
    <div class="accent-strip"></div>
    <div class="photo" role="img" aria-label="Photo of a bright renovated open-plan living and dining room beside two builders in navy hoodies reviewing plans at a timber-framed site"></div>

    <div class="brand">
      <div class="brand-square"></div>
      <div class="brand-name">VELM BUILD</div>
    </div>

    <h1 class="slogan">Don’t move,<br>re-imagine</h1>

    <div class="rule"></div>

    <div class="contact">
      <span class="contact-phone">(+61) 491 570 148</span>
      <span class="contact-web">www.velmbuild.com.au</span>
    </div>
  </div>
</div>
</body>
</html>
```